FUNDRAISER FLYER For Tshirt Business

I would like a front and back flyer advertising fundraising for my print on demand business(KIND THREAD CO) I would like an eye catching color scheme. I don't want it to be cluttered the font should be bold. I am attaching a list of things I need included, please use this as informational that I need on the flyer but not for direction and style. Quick turnaround time. Please add our Instagram and FB info to Flyer with Contact Info

Target Market(s)

Organizations looking to add to their capital by doing fundraising.

Industry/Entity Type

Organization

Requirements
Must have
• Information provided make sure the packages is easily defined
Nice to have
• A key information
Should not have
• Do not copy the images provided. I didn’t not like this layout.

```html
<!DOCTYPE html>
<html lang="en">
<head>
<meta charset="utf-8">
<title>Kind Thread Co – Fundraiser Flyer</title>
<link href="https://fonts.googleapis.com/css2?family=Montserrat:ital,wght@0,600;0,700;0,800;0,900;1,700;1,800&display=swap" rel="stylesheet">
<style>
  :root {
    --stage: #5d5e75;
    --ink-dark: #141010;
    --deep-red: #3a0606;
    --brand-red: #e01b1b;
    --hot-orange: #f7a21a;
    --flame: #f05a12;
    --navy: #1b1f5c;
    --paper: #f1f1f1;
    --silver: #e9e9e9;
    --gold: #efcf3a;
    --gold-deep: #d9b21f;
    --plat: #151515;
    --contact-yellow: #e8c23a;
    --white: #ffffff;
  }
  * { box-sizing: border-box; margin: 0; padding: 0; }
  html, body { width: 1200px; height: 800px; overflow: hidden; }
  body {
    background: radial-gradient(ellipse at center, #7a7b94 0%, var(--stage) 55%, #3e3f50 100%);
    font-family: "Montserrat", sans-serif;
    position: relative;
  }
  .flyer {
    position: absolute;
    top: 100px;
    width: 424px;
    height: 600px;
    overflow: hidden;
    box-shadow: 0 14px 34px rgba(0,0,0,.45);
  }

  /* ---------- Front: packages ---------- */
  .flyer--packages {
    left: 150px;
    background: linear-gradient(160deg, #2a1a0c 0%, var(--deep-red) 45%, var(--ink-dark) 80%, #2b2b2b 100%);
    color: var(--white);
  }
  .flyer--packages .backdrop { position: absolute; inset: 0; }
  .headline-contact {
    position: absolute; top: 34px; left: 0; right: 0;
    text-align: center; color: var(--brand-red);
    font-weight: 900; font-size: 30px; letter-spacing: 1px;
    text-shadow: 0 0 2px #fff;
  }
  .intro {
    position: absolute; top: 80px; left: 0; right: 0;
    text-align: center; font-weight: 800; font-size: 10.5px; line-height: 1.55;
    text-transform: uppercase;
  }
  .headline-store {
    position: absolute; top: 140px; left: 0; right: 0;
    text-align: center; color: var(--brand-red);
    font-weight: 900; font-size: 27px; line-height: 1.1;
    text-shadow: 0 0 2px #fff;
  }
  .packages {
    position: absolute; top: 240px; left: 18px; right: 18px;
    display: flex; gap: 12px;
  }
  .package {
    flex: 1; height: 220px; border-radius: 10px;
    display: flex; flex-direction: column; align-items: center;
    overflow: hidden; box-shadow: 0 6px 14px rgba(0,0,0,.5);
  }
  .package__name {
    font-weight: 900; font-size: 17px; padding: 10px 0 6px; letter-spacing: .5px;
  }
  .package__shirts {
    width: 100%; height: 70px;
    background: linear-gradient(120deg, #f7a21a 0%, #f28c0f 55%, var(--navy) 56%, #12163f 100%);
  }
  .package__terms {
    list-style: none; text-align: center; font-weight: 700;
    font-size: 8.5px; line-height: 1.75; padding: 8px 4px; text-transform: uppercase;
  }
  .package--silver { background: var(--silver); color: #111; }
  .package--gold { background: var(--gold); color: #111; }
  .package--gold .package__name { padding: 6px 0 10px; }
  .package--platinum { background: var(--plat); color: var(--white); }
  .package--platinum .package__name { color: var(--gold); }
  .contact {
    position: absolute; left: 24px; bottom: 30px;
    color: var(--contact-yellow); font-weight: 600; font-size: 11.5px; line-height: 1.45;
    font-style: normal;
  }

  /* ---------- Back: benefits ---------- */
  .flyer--benefits {
    left: 626px;
    background: linear-gradient(135deg, #d9141a 0%, var(--flame) 45%, var(--hot-orange) 100%);
  }
  .flyer--benefits .triangle { position: absolute; inset: 0; }
  .brand {
    position: absolute; top: 40px; right: 30px;
    display: flex; flex-direction: column; align-items: center; gap: 8px;
    color: var(--white); font-weight: 800; font-size: 15px; letter-spacing: .5px;
  }
  .brand__dot { width: 30px; height: 30px; border-radius: 50%; border: 3px solid var(--white); }
  .shirt-mockup {
    position: absolute; top: 108px; right: 28px; width: 110px; height: 138px;
    border-radius: 10px;
    background: linear-gradient(160deg, #ff9d12 0%, #f58a0c 58%, var(--navy) 60%, #10143c 100%);
  }
  .benefits-title {
    position: absolute; top: 124px; left: 108px;
    background: var(--navy); color: var(--white);
    font-weight: 900; font-style: italic; font-size: 22px;
    padding: 6px 34px 6px 12px;
    clip-path: polygon(0 0, 88% 0, 100% 100%, 0 100%);
  }
  .benefits {
    position: absolute; top: 168px; left: 30px; width: 364px;
    list-style: none; color: var(--navy);
    font-weight: 700; font-style: italic; font-size: 9.4px; line-height: 1.55;
    text-transform: uppercase;
  }
  .benefits li { position: relative; padding-left: 12px; }
  .benefits li::before {
    content: ""; position: absolute; left: 0; top: 3px;
    width: 6px; height: 6px; background: var(--brand-red);
  }
  .benefits li.no-mark::before { display: none; }
  .win {
    position: absolute; top: 452px; left: 0; right: 0; text-align: center;
    color: var(--hot-orange); font-weight: 900; font-style: italic; font-size: 58px;
    letter-spacing: -1px;
    text-shadow: 0 0 8px rgba(230,20,20,.9), 0 0 3px rgba(230,20,20,1);
  }
  .win-sub {
    position: absolute; top: 532px; left: 0; right: 0; text-align: center;
    color: var(--brand-red); font-weight: 900; font-size: 24px;
  }
</style>
</head>
<body>

<section class="flyer flyer--packages">
  <svg class="backdrop" viewBox="0 0 424 600" aria-hidden="true">
    <polygon points="212,200 60,600 364,600" fill="#3a3a3a" opacity=".35"/>
    <polygon points="330,220 424,180 424,600 300,600" fill="#444" opacity=".25"/>
  </svg>
  <h2 class="headline-contact">CONTACT US NOW !</h2>
  <p class="intro">To build your free store to earn money for<br>your organization or group !<br>Call for more info !</p>
  <h1 class="headline-store">BUILD YOUR TSHIRT STORE<br>FUNDRAISER</h1>

  <div class="packages">
    <article class="package package--silver">
      <h3 class="package__name">SILVER</h3>
      <div class="package__shirts" role="img" aria-label="Orange and navy t-shirts"></div>
      <ul class="package__terms">
        <li>2 shirt choice</li><li>1 design</li><li>1 color</li>
        <li>Sell : 1-25 earn 20 %</li><li>25-50 earn 25%</li><li>50-100 earn 30%</li>
      </ul>
    </article>
    <article class="package package--gold">
      <ul class="package__terms">
        <li>2 shirt choice</li><li>2 design</li><li>3 color</li>
        <li>Sell : 1-25 earn 15 %</li><li>25-50 earn 20%</li><li>50-100 earn 25%</li>
      </ul>
      <div class="package__shirts" role="img" aria-label="Orange and navy t-shirts"></div>
      <h3 class="package__name">GOLD</h3>
    </article>
    <article class="package package--platinum">
      <h3 class="package__name">PLATINUM</h3>
      <div class="package__shirts" role="img" aria-label="Orange and navy t-shirts"></div>
      <ul class="package__terms">
        <li>2 shirt choice</li><li>3 design</li><li>Full color</li>
        <li>1-25 earn 25%</li><li>25-50 earn 30%</li><li>50-100 earn 35%</li>
      </ul>
    </article>
  </div>

  <address class="contact">
    www.kindthreadco.com<br>shop@kindthreadco.com<br>555-017-3690
  </address>
</section>

<section class="flyer flyer--benefits">
  <svg class="triangle" viewBox="0 0 424 600" aria-hidden="true">
    <polygon points="232,48 0,560 0,600 424,600 424,540" fill="var(--paper)"/>
  </svg>
  <div class="shirt-mockup" role="img" aria-label="Orange and navy t-shirt mockup with space for your design and logo"></div>
  <div class="brand">
    <span class="brand__dot"></span>
    <span class="brand__name">KIND THREAD CO</span>
  </div>

  <h2 class="benefits-title">BENEFITS</h2>
  <ul class="benefits">
    <li>No stock</li>
    <li>No upfront cost</li>
    <li>No order form</li>
    <li>Instant order notification</li>
    <li>Daily order summary</li>
    <li>No money exchange / collecting</li>
    <li>No customer contact ( covid approved)</li>
    <li class="no-mark">No risk</li>
    <li>No headaches</li>
    <li>Tshirts are an easy sale for the right purpose</li>
    <li>Invest less time with sales and more time connecting with your audience to invest in a worthy cause</li>
    <li>All fullfillment and shipping handled by Kind Thread Co</li>
    <li>Online platform</li>
    <li>Gain revenue for your organization</li>
  </ul>

  <p class="win">WIN WIN</p>
  <p class="win-sub">SITUATION YOU CANT LOSE</p>
</section>

</body>
</html>
```